New emergency medical service needs a marketing flyer for prospective customers

We need a tri fold brochure on an 8.5 X 11 stock for a new emergency medical service in Pennsylvania. We provide basic first aid and now Covid-19 pre screening and temperature monitoring for special events, large gatherings and businesses. Examples of these would be but not limited to: Sporting events, carnivals, festivals, craft shows, warehouses, churches, manufacturing facilities, industrial buildings, large construction sites, multi occupancy officer buildings. The market for this is pretty much untouched and endless. we would like to use gray as the back ground color and obviously our logo. The final design should grab their attention and communicate the importance of having trained and certified professionals at their event or facility. We want to give them that piece of mind they are in good hands with us.

Target Market(s)

primary focus is going to be on businesses with large offices, large buildings or lots of foot traffic in and out of the building

Requirements
Must have
• gray background, pictures, company phone # , company web site, and contact email address. I will provide all that information to the winner to add at the end.
Nice to have
• pictures that covers the whole front cover with logo at top

```html
<!DOCTYPE html>
<html lang="en">
<head>
<meta charset="utf-8">
<title>Ridgeline Medical Services – Tri-fold Brochure</title>
<link href="https://fonts.googleapis.com/css2?family=Lato:wght@400;700;900&display=swap" rel="stylesheet">
<style>
:root{
  --stage:#c9cacc;
  --teal:#1fb9a3;
  --teal-soft:#3fc0ab;
  --navy:#2e3192;
  --paper:#ecedea;
  --paper-mid:#d6d6d6;
  --ink:#1d1d1d;
  --grey-text:#444;
  --white:#fff;
}
*{margin:0;padding:0;box-sizing:border-box}
html,body{width:1200px;height:1200px;overflow:hidden;background:var(--stage);font-family:'Lato',sans-serif}
.sheet{position:absolute;width:740px;height:572px;overflow:hidden;box-shadow:0 6px 18px rgba(0,0,0,.25)}
.sheet--outside{left:40px;top:28px}
.sheet--inside{left:420px;top:610px;background:var(--paper)}
.panel{position:absolute;top:0;width:247px;height:572px;overflow:hidden}
.panel--1{left:0}.panel--2{left:247px}.panel--3{left:494px}
.fold{position:absolute;top:0;width:1px;height:100%;background:rgba(0,0,0,.08)}
.photo{position:absolute}

/* outside */
.paramedic-photo{inset:0;background:linear-gradient(170deg,#8d9098 0%,#7d8599 45%,#6a78a6 100%)}
.trained__title{position:absolute;left:26px;top:300px;color:var(--white);font-size:20px;font-weight:700;line-height:1.3}
.trained__body{position:absolute;left:26px;top:420px;width:200px;color:var(--white);font-size:14px;line-height:1.35}
.panel--2.contact{background:var(--teal)}
.contact svg{position:absolute;inset:0}
.contact__inner{position:absolute;left:0;top:200px;width:247px;text-align:center}
.contact__label{color:var(--navy);font-size:16px;font-weight:700}
.brand{color:var(--navy);font-weight:900;display:inline-flex;align-items:center;gap:7px}
.brand__dot{width:14px;height:14px;border-radius:50%;background:var(--navy)}
.contact .brand{font-size:19px;margin:12px 0 8px;line-height:1.1}
.contact__web{color:var(--navy);font-size:14px}
.contact__mail,.contact__phone{color:var(--grey-text);font-size:11px;margin-top:3px}
.cover{background:var(--paper)}
.cover__brand{position:absolute;top:28px;left:0;width:247px;text-align:center}
.cover .brand{font-size:20px}
.cover__headline{position:absolute;top:80px;left:0;width:247px;text-align:center;color:var(--teal);font-size:19px;font-weight:700;line-height:1.25}
.staff-photo{left:0;top:150px;width:247px;height:422px;background:linear-gradient(180deg,#e6e7e6 0%,#c9b2a2 35%,#5b6f8f 70%,#274579 100%)}

/* inside */
.welcome__faded{inset:0;background:linear-gradient(180deg,#dcdcdc,#e8e8e6)}
.welcome svg,.team svg,.gallery svg{position:absolute;inset:0}
.welcome__brand{position:absolute;top:40px;left:0;width:247px;text-align:center}
.welcome .brand{font-size:21px}
.welcome__headline{position:absolute;left:45px;top:140px;width:190px;color:var(--teal);font-size:19px;font-weight:700;line-height:1.3}
.mask-portrait{left:60px;top:330px;width:140px;height:140px;border-radius:50%;background:radial-gradient(circle at 50% 40%,#e9e6e2,#b9c3d2 60%,#7d8fb0)}
.team__title{position:absolute;left:22px;top:34px;color:var(--teal);font-weight:700;line-height:1}
.team__title span{display:block}
.team__title .big{font-size:33px}
.team__title .small{font-size:21px;margin-top:4px}
.team__body{position:absolute;left:22px;top:108px;width:212px;color:var(--ink);font-size:9.5px;line-height:1.25}
.team__body p{margin-bottom:12px}
.team__list-head{font-size:12px;font-weight:700;margin-bottom:2px}
.team__list{list-style:none;font-size:10px;line-height:1.3}
.snapshot{position:absolute;border:5px solid var(--white);box-shadow:0 3px 8px rgba(0,0,0,.3)}
.snap--ambulance{left:14px;top:340px;width:185px;height:125px;transform:rotate(3deg);background:linear-gradient(180deg,#cfd6d0 0%,#d6d26a 40%,#5d8a45 70%,#4f7d3c 100%)}
.snap--tent{left:36px;top:28px;width:195px;height:140px;transform:rotate(-4deg);background:linear-gradient(160deg,#3c7a6e,#2f6c60 55%,#3d8a4d)}
.snap--station{left:-10px;top:196px;width:225px;height:140px;transform:rotate(5deg);background:linear-gradient(180deg,#f0f0ee,#8c8f8a 55%,#5d5246)}
.snap--fleet{left:20px;top:400px;width:220px;height:150px;transform:rotate(-3deg);background:linear-gradient(180deg,#6c8b50,#4d6b37 40%,#dcdcd0 65%,#3f6b2e)}
</style>
</head>
<body>

<section class="sheet sheet--outside">
  <div class="panel panel--1 trained">
    <div class="photo paramedic-photo" role="img" aria-label="Paramedic in face shield, mask and protective gown"></div>
    <h2 class="trained__title">Our Medical Teams<br>Are TRAINED and<br>CERTIFIED<br>Paramedics</h2>
    <p class="trained__body">For events/venues/facilities which require medical teams with advanced care paramedics skills</p>
  </div>

  <div class="panel panel--2 contact">
    <svg width="247" height="572" viewBox="0 0 247 572"><ellipse cx="150" cy="290" rx="245" ry="250" fill="var(--paper-mid)"/></svg>
    <div class="contact__inner">
      <p class="contact__label">Contact Us</p>
      <div class="brand"><span class="brand__dot"></span>Ridgeline Medical<br>Services</div>
      <p class="contact__web">ridgelinemedical.com</p>
      <p class="contact__mail">hello@ridgelinemedical.com</p>
      <p class="contact__phone">555-0142</p>
    </div>
  </div>

  <div class="panel panel--3 cover">
    <div class="cover__brand"><span class="brand"><span class="brand__dot"></span>Ridgeline Medical</span></div>
    <h1 class="cover__headline">Medical Services<br>That You Can Trust</h1>
    <div class="photo staff-photo" role="img" aria-label="Smiling medic in navy scrubs with a doctor behind him"></div>
  </div>
  <div class="fold" style="left:247px"></div><div class="fold" style="left:494px"></div>
</section>

<section class="sheet sheet--inside">
  <div class="panel panel--1 welcome">
    <div class="photo welcome__faded" role="img" aria-label="Faded background photo of medical staff"></div>
    <svg width="247" height="572" viewBox="0 0 247 572"><path d="M0 300 C30 420 130 470 247 420 L247 572 L0 572 Z" fill="var(--teal-soft)"/></svg>
    <div class="welcome__brand"><span class="brand"><span class="brand__dot"></span>Ridgeline Medical</span></div>
    <h2 class="welcome__headline">We work with each of our clients to create a safe environment for attendees and employees</h2>
    <div class="photo mask-portrait" role="img" aria-label="Medic wearing a face shield and respirator mask"></div>
  </div>

  <div class="panel panel--2 team">
    <svg width="247" height="572" viewBox="0 0 247 572"><path d="M0 400 C80 380 170 370 247 340 L247 572 L0 572 Z" fill="var(--teal-soft)"/></svg>
    <h2 class="team__title"><span class="big">Professional</span><span class="small">Medical Team</span></h2>
    <div class="team__body">
      <p>Understanding that all events and venues are unique in size and scope our team of dedicated event medical services specialists will work with you to develop the right size medical team with the expertise required for your event/venue.</p>
      <p>Our team of corporate event medical professionals specialize in providing high quality medical services best suited for corporate events and venues.</p>
      <p class="team__list-head">Our corporate events clientele include:</p>
      <ul class="team__list">
        <li>- Businesses</li><li>- Professional sporting facilities</li><li>- Conference/concert facilities</li><li>- Promotional companies</li><li>- Event planners</li>
      </ul>
    </div>
    <div class="snapshot snap--ambulance" role="img" aria-label="Air ambulance helicopter and yellow ambulance on a field"></div>
  </div>

  <div class="panel panel--3 gallery">
    <svg width="247" height="572" viewBox="0 0 247 572"><path d="M0 350 C90 330 170 330 247 325 L247 572 L0 572 Z" fill="var(--teal-soft)"/></svg>
    <div class="snapshot snap--tent" role="img" aria-label="Medics seated outside a green first aid tent"></div>
    <div class="snapshot snap--station" role="img" aria-label="Medical team preparing a treatment station inside a marquee"></div>
    <div class="snapshot snap--fleet" role="img" aria-label="Medics standing beside response vehicles on grass"></div>
  </div>
  <div class="fold" style="left:247px"></div><div class="fold" style="left:494px"></div>
</section>

</body>
</html>
```